Website for enterprise software start-up

We need a new Wordpress website. We are an early stage start-up focused on mobile video technology for cellular operators. The audience is strategy, marketing and customer acquisition execs from the operators.

The purpose of the site is to act as a sales brochure and capture leads. A demo app can be downloaded from the current site, want to put that behind a contact form.

Current website is at www.brellowmo.tv. Similar number of pages. Looking for a clean design template, with minimal customization. Blog will remain as is.

Want to be able to modify the copy via Wordpress. Reference designs I like: vandrisk.com, tallowquarrymetric.com

Target Market(s)

Mobile operators and MVNOs in the US and Asia Pacific regions

Industry/Entity Type

Business Software

Coding

Coded - Design and coding required

Number of Pages Required

4 page

Font styles to use
Sans Serif

Colors
f78f20

Requirements
Must have
• Form for downloading sample apps.
• Landing page with image, Product, Blog, About, Contact
• Team page

```html
<!DOCTYPE html>
<html lang="en">
<head>
<meta charset="utf-8">
<title>Brellowmo Media</title>
<link rel="stylesheet" href="https://fonts.googleapis.com/css2?family=Ubuntu:wght@400;500&family=Open+Sans:wght@400;600&display=swap">
<style>
:root{
  --orange:#e27618;
  --orange-dark:#c9650f;
  --ink:#2b2b2b;
  --text:#555;
  --muted:#999;
  --line:#e3e3e3;
  --grey-band:#f2f2f2;
  --white:#fff;
  --badge:#1c1c1c;
}
*{box-sizing:border-box;margin:0;padding:0}
html,body{width:1200px;height:2616px;overflow:hidden}
body{position:relative;background:var(--white);font-family:"Open Sans",Arial,sans-serif;color:var(--text)}
.abs{position:absolute}
.heading{font-family:"Ubuntu",Arial,sans-serif;font-weight:400;color:var(--ink);font-size:30px}
.heading em{font-style:normal;color:var(--orange)}
.btn{position:absolute;display:flex;align-items:center;justify-content:center;gap:10px;background:var(--orange);color:var(--white);font-size:12px;border-radius:2px;border:1px solid var(--orange-dark)}
.btn .tri{width:0;height:0;border-left:8px solid var(--white);border-top:6px solid transparent;border-bottom:6px solid transparent}
.side-label{position:absolute;writing-mode:vertical-rl;font-family:"Ubuntu",Arial,sans-serif;font-size:22px;letter-spacing:4px;color:#e4e4e4}
.slider-arrow{position:absolute;width:14px;height:28px}

/* hero */
.hero{position:absolute;left:0;top:0;width:1200px;height:523px;background:linear-gradient(100deg,#3a2c24 0%,#7a6659 30%,#c9bfb6 60%,#eee9e4 100%)}
.nav{position:absolute;left:162px;top:23px;width:876px;height:90px;background:rgba(255,255,255,.96);box-shadow:0 2px 8px rgba(0,0,0,.2);border-radius:2px}
.brand{position:absolute;left:24px;top:24px;display:flex;align-items:center;gap:10px;font-family:"Ubuntu",Arial,sans-serif;font-size:32px;font-weight:500;color:var(--orange)}
.brand .mark{width:38px;height:38px;background:var(--orange)}
.nav-links{position:absolute;left:396px;top:37px;display:flex;gap:33px;font-size:11px;color:#333}
.nav-links .active{color:var(--orange)}
.login{left:785px;top:30px;width:70px;height:26px;font-size:11px}
.hero-title{right:178px;top:232px;text-align:right;font-family:"Ubuntu",Arial,sans-serif;font-weight:400;font-size:35px;line-height:42px;color:#222}
.hero-sub{right:178px;top:322px;width:270px;text-align:right;font-size:11px;line-height:15px;color:#222}
.store{position:absolute;top:364px;height:33px;background:var(--badge);border:1px solid #555;border-radius:4px;box-shadow:0 1px 2px rgba(0,0,0,.25)}
.sample{left:900px;top:364px;width:122px;height:33px}

/* about */
.about-copy{left:162px;top:644px;width:574px;font-size:11.5px;line-height:21px}
.about-copy p+p{margin-top:10px}
.about-phone{left:770px;top:558px;width:240px;height:323px;background:linear-gradient(160deg,#f6f6f6,#d9d9d9);border-radius:20px}

/* product band */
.product{position:absolute;left:0;top:881px;width:1200px;height:474px;background:var(--orange);overflow:hidden}
.notch{position:absolute;left:582px;top:0}
.product-phones{left:209px;top:61px;width:262px;height:357px;background:linear-gradient(160deg,#f4f4f4,#cfc6d6);border-radius:24px}
.dots{position:absolute;display:flex;flex-direction:column;gap:9px}
.dots span{width:13px;height:13px;border-radius:50%;background:rgba(255,255,255,.35)}
.dots .on{background:rgba(255,255,255,.85)}
.product .heading{position:absolute;left:506px;top:75px;color:var(--white);display:flex;align-items:center;gap:12px}
.features{position:absolute;left:506px;top:145px;width:520px;list-style:none;color:var(--white);font-size:12.5px;line-height:18px}
.features li{position:absolute;left:0;display:flex;gap:12px;width:520px}
.features svg{flex:none;margin-top:2px}

/* updates */
.date{left:162px;top:1490px;width:56px;height:88px;border-right:1px solid var(--line);text-align:center}
.date b{display:block;font-family:"Ubuntu",Arial,sans-serif;font-weight:500;font-size:20px;color:var(--orange);margin-top:22px}
.date span{font-size:11px}
.post-title{left:244px;top:1474px;font-family:"Ubuntu",Arial,sans-serif;font-weight:400;font-size:16px;color:#222}
.post-meta{left:244px;top:1506px;font-size:10px;font-style:italic;color:var(--orange)}
.post-excerpt{left:244px;top:1530px;width:410px;font-size:11px;line-height:19px}
.post-image{left:696px;top:1474px;width:293px;height:165px;background:linear-gradient(120deg,#d9d3cc,#8d7f72 60%,#5b5048);box-shadow:2px 3px 5px rgba(0,0,0,.3)}

/* team */
.team{position:absolute;left:0;top:1695px;width:1200px;height:403px;background:var(--grey-band)}
.member{position:absolute;top:105px;width:190px;height:244px;background:linear-gradient(180deg,#dedede,#b9b9b9);overflow:hidden}
.member .name{position:absolute;left:0;bottom:0;width:100%;height:52px;background:rgba(40,40,40,.85);color:var(--white);display:flex;align-items:center;justify-content:center;font-family:"Ubuntu",Arial,sans-serif;font-size:13px}
.member .name.big{font-size:18px}
.member.open{background:var(--orange);color:var(--white);text-align:center;border:1px solid var(--orange-dark)}
.member.open h3{font-family:"Ubuntu",Arial,sans-serif;font-weight:500;font-size:20px;margin-top:32px}
.member.open p{font-size:11.5px;line-height:18px;margin:8px 16px 0}
.socials{display:flex;justify-content:center;gap:6px;margin-top:12px}
.socials span{width:20px;height:20px;border-radius:50%;background:var(--white)}

/* partners & contact */
.tile{position:absolute;width:110px;height:82px;border:1px solid var(--line);background:var(--white)}
.tile i{position:absolute;left:25px;top:26px;width:60px;height:30px;background:#d6d6d6;border-radius:4px}
.dots.grey span{background:#cfcfcf}
.dots.grey .on{background:#333}
.cert{left:162px;top:2442px;width:196px;height:69px;border:1px solid #ddd;border-radius:8px;background:#f7f7f7;display:flex;align-items:center;gap:12px;padding-left:8px;font-family:"Ubuntu",Arial,sans-serif;font-size:18px;color:#333}
.cert .mark{width:52px;height:52px;background:var(--orange);border-radius:6px}
.cert-note{left:375px;top:2458px;width:230px;font-size:11px;line-height:19px}
.cert-note a{color:var(--orange);text-decoration:none}
.field{position:absolute;left:668px;width:370px;height:35px;border:1px solid var(--line);font-size:10.5px;color:#aaa;padding:9px 14px}
.send{left:668px;top:2478px;width:131px;height:33px}

/* footer */
.footer{position:absolute;left:0;top:2564px;width:1200px;height:52px;background:var(--orange);color:var(--white);font-size:11px}
.footer .copy{position:absolute;left:162px;top:19px}
.footer .follow{position:absolute;left:784px;top:13px;display:flex;align-items:center;gap:7px}
.footer .follow span{width:25px;height:25px;border-radius:50%;border:1.5px solid var(--white)}
</style>
</head>
<body>

<header class="hero">
  <div class="abs" style="inset:0" role="img" aria-label="Hero photo: a person holding a smartphone playing a video"></div>
  <svg class="slider-arrow" style="left:94px;top:281px;width:34px;height:66px" viewBox="0 0 34 66"><path d="M32 2 2 33l30 31" fill="none" stroke="#fff" stroke-width="2"/></svg>
  <svg class="slider-arrow" style="left:1070px;top:281px;width:34px;height:66px" viewBox="0 0 34 66"><path d="M2 2l30 31L2 64" fill="none" stroke="#fff" stroke-width="2"/></svg>
  <nav class="nav">
    <div class="brand"><span class="mark"></span>Brellowmo Media</div>
    <div class="nav-links">
      <span class="active">ABOUT</span><span>PRODUCT</span><span>OUR TEAM</span><span>BLOG</span><span>CONTACT</span>
    </div>
    <div class="btn login">LOGIN <span class="tri"></span></div>
  </nav>
  <h1 class="abs hero-title">High Quality<br>Mobile Engagement™</h1>
  <p class="abs hero-sub">We engage mobile audiences with the right video content at the perfect moment.</p>
  <div class="store" style="left:663px;width:106px" role="img" aria-label="App download badge"></div>
  <div class="store" style="left:781px;width:107px" role="img" aria-label="App download badge"></div>
  <div class="btn sample">Sample Apps <span class="tri"></span></div>
</header>

<section class="about">
  <h2 class="abs heading" style="left:162px;top:574px;display:flex;align-items:center;gap:10px">We are <span style="width:30px;height:30px;background:var(--orange)"></span><em style="font-weight:500">Brellowmo</em></h2>
  <div class="abs about-copy">
    <p>Brellowmo Media exists because video consumption is trending away from TV towards mobile, and because mobile media is trending away from pull consumption towards push consumption - where each user is notified of personalized content at the perfect moment.</p>
    <p>We started Brellowmo Media to help media publishers navigate these trends, solving the technical challenges of delivering personalized and highest quality mobile video experiences, and seizing the economic opportunity of attracting premium brand advertising.</p>
  </div>
  <div class="btn" style="left:162px;top:795px;width:114px;height:32px">Read More <span class="tri"></span></div>
  <div class="abs about-phone" role="img" aria-label="Photo of a hand holding a smartphone showing the app"></div>
  <div class="side-label" style="left:1016px;top:560px">— about —</div>
</section>

<section class="product">
  <svg class="notch" width="36" height="18" viewBox="0 0 36 18"><path d="M0 0h36L18 18z" fill="#fff"/><path d="M9 4h18l-9 9z" fill="var(--orange)"/></svg>
  <div class="dots" style="left:163px;top:207px"><span></span><span class="on"></span><span></span></div>
  <div class="abs product-phones" role="img" aria-label="Two smartphones showing a push video notification"></div>
  <h2 class="heading"><svg width="14" height="18" viewBox="0 0 14 18"><rect x="0" y="0" width="3" height="18" fill="#fff"/><path d="M14 0v18L5 9z" fill="#fff"/></svg>Push Video Notifications</h2>
  <ul class="features">
    <li style="top:0"><svg width="12" height="12" viewBox="0 0 12 12"><circle cx="6" cy="6" r="5" fill="none" stroke="#fff"/><path d="M3.5 6l2 2 3-4" fill="none" stroke="#fff"/></svg>Personalised flawless HD videos, revealed at the perfect moment, as rich media notifications.</li>
    <li style="top:59px"><svg width="12" height="12" viewBox="0 0 12 12"><circle cx="6" cy="6" r="5" fill="none" stroke="#fff"/><path d="M3.5 6l2 2 3-4" fill="none" stroke="#fff"/></svg>Guarantee your audience never gets frustrated with a poor quality mobile video streaming experience.</li>
    <li style="top:121px"><svg width="12" height="12" viewBox="0 0 12 12"><circle cx="6" cy="6" r="5" fill="none" stroke="#fff"/><path d="M3.5 6l2 2 3-4" fill="none" stroke="#fff"/></svg>Instant video playback, zero buffering, HD quality guaranteed - even when offline.</li>
    <li style="top:164px"><svg width="12" height="12" viewBox="0 0 12 12"><circle cx="6" cy="6" r="5" fill="none" stroke="#fff"/><path d="M3.5 6l2 2 3-4" fill="none" stroke="#fff"/></svg>Content is personalised based on viewer interests and mobile viewing habits.</li>
    <li style="top:206px"><svg width="12" height="12" viewBox="0 0 12 12"><circle cx="6" cy="6" r="5" fill="none" stroke="#fff"/><path d="M3.5 6l2 2 3-4" fill="none" stroke="#fff"/></svg>Monetize with beautiful HD preroll or interstitial ads.</li>
    <li style="top:248px"><svg width="12" height="12" viewBox="0 0 12 12"><circle cx="6" cy="6" r="5" fill="none" stroke="#fff"/><path d="M3.5 6l2 2 3-4" fill="none" stroke="#fff"/></svg>Use your existing content management and hosting systems.</li>
  </ul>
</section>

<section class="updates">
  <h2 class="abs heading" style="left:162px;top:1405px">Latest <em>Updates</em></h2>
  <svg class="slider-arrow" style="left:108px;top:1528px" viewBox="0 0 14 28"><path d="M13 1 1 14l12 13" fill="none" stroke="#ccc" stroke-width="1.5"/></svg>
  <svg class="slider-arrow" style="left:1078px;top:1528px" viewBox="0 0 14 28"><path d="M1 1l12 13L1 27" fill="none" stroke="#ccc" stroke-width="1.5"/></svg>
  <div class="abs date"><b>18</b><span>March</span></div>
  <h3 class="abs post-title">Closing the Gap: Smartphones vs TV</h3>
  <p class="abs post-meta">JUNE 26, 2016 / OWEN HALBERG</p>
  <p class="abs post-excerpt">What's the difference between mobile and television? About $22billion, at least where advertising budgets are concerned. It's known as the "Halden Gap", the difference between time audiences spend on mobile and the total...</p>
  <div class="btn" style="left:244px;top:1599px;width:113px;height:32px">Read More <span class="tri"></span></div>
  <div class="abs post-image" role="img" aria-label="Blog photo: hands holding a smartphone"></div>
  <div class="side-label" style="left:1016px;top:1395px">— Our Blog —</div>
</section>

<section class="team">
  <h2 class="abs heading" style="left:162px;top:47px">Management <em>Team</em></h2>
  <svg class="slider-arrow" style="left:108px;top:210px" viewBox="0 0 14 28"><path d="M13 1 1 14l12 13" fill="none" stroke="#ccc" stroke-width="1.5"/></svg>
  <svg class="slider-arrow" style="left:1078px;top:210px" viewBox="0 0 14 28"><path d="M1 1l12 13L1 27" fill="none" stroke="#ccc" stroke-width="1.5"/></svg>
  <div class="member" style="left:162px" role="img" aria-label="Portrait photo of the company CEO"><div class="name">Company CEO - Owen</div></div>
  <div class="member open" style="left:375px">
    <h3>Lasse</h3>
    <p>c Ut wisi enim ad minim veniam, quis nostrud exerci tation ullamcorper suscipit lobortis nisl ut aliquip ex ea commodo consequat</p>
    <div class="socials"><span></span><span></span><span></span><span></span></div>
  </div>
  <div class="member" style="left:588px" role="img" aria-label="Portrait photo of team member Rafael"><div class="name big">Rafael</div></div>
  <div class="member" style="left:802px" role="img" aria-label="Portrait photo of team member Corin"><div class="name big">Corin SVP</div></div>
  <div class="side-label" style="left:1016px;top:65px;color:#e2e2e2">— Our Team —</div>
</section>

<section class="partners">
  <h2 class="abs heading" style="left:162px;top:2143px">Our <em>Certified Partner</em></h2>
  <div class="dots grey" style="left:168px;top:2250px"><span></span><span></span><span class="on"></span><span></span><span></span></div>
  <div class="tile" style="left:221px;top:2211px"><i></i></div>
  <div class="tile" style="left:363px;top:2211px"><i></i></div>
  <div class="tile" style="left:504px;top:2211px"><i></i></div>
  <div class="tile" style="left:221px;top:2318px"><i></i></div>
  <div class="tile" style="left:363px;top:2318px"><i></i></div>
  <div class="tile" style="left:504px;top:2318px"><i></i></div>
  <div class="abs cert"><span class="mark"></span>Brellowmo</div>
  <p class="abs cert-note"><a>Contact us</a> for details of how to become a Certified Developer Partner.</p>
</section>

<section class="contact">
  <h2 class="abs heading" style="left:668px;top:2143px">Contact <em>Us</em></h2>
  <div class="field" style="top:2206px">Your Name</div>
  <div class="field" style="top:2257px">Your Email</div>
  <div class="field" style="top:2307px">Subject</div>
  <div class="field" style="top:2358px;height:89px">Message</div>
  <div class="btn send">Send Message <span class="tri"></span></div>
</section>

<footer class="footer">
  <span class="copy">Copyright © 2016 Brellowmedia. All rights reserved.</span>
  <div class="follow">Follow Us: <span></span><span></span><span></span><span></span><span></span><span></span></div>
</footer>

</body>
</html>
```